Surviving Domestic Violence Flyer

I need a flyer that "POPS" to attract participants for my research project. I have added the important information on my draft flyer.

```html
<!DOCTYPE html>
<html lang="en">
<head>
<meta charset="utf-8">
<title>Request for Study Participants</title>
<link href="https://fonts.googleapis.com/css2?family=Oswald:wght@600&family=PT+Sans+Narrow:wght@700&family=Open+Sans:wght@400;600&display=swap" rel="stylesheet">
<style>
  :root {
    --page-bg: #ececec;
    --navy: #1f2d8c;
    --subtitle-grey: #5b6068;
    --bullet-grey: #6b7078;
    --body-blue: #2f7cc6;
    --detail-grey: #6d7279;
    --sky-top: #b8c8da;
    --sky-mid: #e6ecf2;
    --sea: #c4cfda;
    --sand-light: #ddd7cd;
    --sand-dark: #cbc1b2;
    --tab-bg: rgba(255,255,255,0.55);
    --tab-line: rgba(120,120,120,0.55);
    --tab-text: #3a3d42;
  }
  * { margin: 0; padding: 0; box-sizing: border-box; }
  html, body { width: 1200px; height: 900px; overflow: hidden; }
  body { background: var(--page-bg); position: relative; font-family: "Open Sans", Arial, sans-serif; }

  .flyer {
    position: absolute; left: 282px; top: 28px;
    width: 642px; height: 836px; overflow: hidden;
  }
  .flyer__photo {
    position: absolute; inset: 0;
    background: linear-gradient(180deg, var(--sky-top) 0%, var(--sky-mid) 45%, #eef2f5 62%, var(--sea) 70%, var(--sand-light) 78%, var(--sand-dark) 100%);
  }
  .flyer__content { position: absolute; inset: 0; }

  .flyer__title {
    font-family: "Oswald", "Arial Narrow", sans-serif; font-weight: 600;
    color: var(--navy); font-size: 33px; letter-spacing: 0.5px;
    text-align: center; margin-top: 44px; line-height: 40px;
  }
  .flyer__subtitle {
    font-family: "PT Sans Narrow", "Arial Narrow", sans-serif; font-weight: 700;
    color: var(--subtitle-grey); font-size: 24px; line-height: 30px;
    text-align: center; margin-top: 4px;
  }
  .questions {
    list-style: none; margin: 14px 0 0 44px; width: 580px;
    color: var(--bullet-grey); font-size: 18.5px; line-height: 26px;
  }
  .questions li { position: relative; padding-left: 32px; margin-bottom: 4px; }
  .questions li::before {
    content: ""; position: absolute; left: 2px; top: 10px;
    width: 8px; height: 8px; border-radius: 50%; background: var(--bullet-grey);
  }

  .details {
    position: absolute; left: 73px; top: 372px; width: 330px;
    font-size: 11px; line-height: 17px;
  }
  .details__note { color: var(--body-blue); }
  .details__note--eligibility { margin-bottom: 7px; }
  .details__note--contact { margin-bottom: 27px; }
  .details__label { color: var(--navy); font-size: 13px; font-weight: 600; line-height: 18px; margin-top: 6px; }
  .details__value { color: var(--detail-grey); }

  .tear-tabs {
    position: absolute; left: 24px; right: 0; top: 681px; bottom: 0;
    display: flex;
  }
  .tear-tab {
    flex: 1; background: var(--tab-bg);
    border-left: 1px dashed var(--tab-line); border-top: 1px solid var(--tab-line);
    display: flex; align-items: center; justify-content: center;
  }
  .tear-tab:first-child { border-left: 1px solid var(--tab-line); }
  .tear-tab__text {
    writing-mode: vertical-rl; transform: rotate(180deg);
    color: var(--tab-text); font-size: 11px; line-height: 14px; white-space: nowrap;
  }
  .tear-tab__phone { font-weight: 600; }
</style>
</head>
<body>
  <div class="flyer">
    <div class="flyer__photo" role="img" aria-label="Photo of a woman with long dark hair seen from behind, sitting on a beach and looking out over calm sea under a pale hazy sky"></div>
    <div class="flyer__content">
      <h1 class="flyer__title">REQUEST FOR STUDY PARTICIPANTS</h1>
      <h2 class="flyer__subtitle">Efficiency Of Resources Available To Survivors<br>Of Intimate Partner Abuse</h2>
      <ul class="questions">
        <li>Are you eighteen years of age or older?</li>
        <li>Have you been a victim of domestic violence?</li>
        <li>Have you sought assistance with abuse in the last 12 months?</li>
        <li>Are you still in contact with the person who abused you?</li>
        <li>Are you willing and open to discussing your experience with abuse and your attempts to access services or resources?</li>
      </ul>
      <div class="details">
        <p class="details__note details__note--eligibility">If you answered yes to all of these questions, you may be eligible to participate in a study to better understand the resourses needed and services expected for survivors of domestic violence.</p>
        <p class="details__note details__note--contact">Please contact Dana Whitfield at 1(555)014-2290 or<br>via e-mail survivorstudy@inboxmail.net for additional information.</p>
        <p class="details__note">Participants will be compensated for their time.</p>
        <p class="details__label">Principal Investigator</p>
        <p class="details__value">Dana Whitfield</p>
        <p class="details__label">Institutional Affiliation</p>
        <p class="details__value">Lakeshore State University,<br>Dept. of Criminology, Law and Justice</p>
        <p class="details__label">Contact Address</p>
        <p class="details__value">Post Office Box 482150, Riverton, IL, 60611</p>
      </div>
    </div>
    <div class="tear-tabs">
      <div class="tear-tab"><p class="tear-tab__text">Survivor Resources Study<br><span class="tear-tab__phone">1(555)014-2290</span></p></div>
      <div class="tear-tab"><p class="tear-tab__text">Survivor Resources Study<br><span class="tear-tab__phone">1(555)014-2290</span></p></div>
      <div class="tear-tab"><p class="tear-tab__text">Survivor Resources Study<br><span class="tear-tab__phone">1(555)014-2290</span></p></div>
      <div class="tear-tab"><p class="tear-tab__text">Survivor Resources Study<br><span class="tear-tab__phone">1(555)014-2290</span></p></div>
      <div class="tear-tab"><p class="tear-tab__text">Survivor Resources Study<br><span class="tear-tab__phone">1(555)014-2290</span></p></div>
      <div class="tear-tab"><p class="tear-tab__text">Survivor Resources Study<br><span class="tear-tab__phone">1(555)014-2290</span></p></div>
      <div class="tear-tab"><p class="tear-tab__text">Survivor Resources Study<br><span class="tear-tab__phone">1(555)014-2290</span></p></div>
      <div class="tear-tab"><p class="tear-tab__text">Survivor Resources Study<br><span class="tear-tab__phone">1(555)014-2290</span></p></div>
      <div class="tear-tab"><p class="tear-tab__text">Survivor Resources Study<br><span class="tear-tab__phone">1(555)014-2290</span></p></div>
      <div class="tear-tab"><p class="tear-tab__text">Survivor Resources Study<br><span class="tear-tab__phone">1(555)014-2290</span></p></div>
    </div>
  </div>
</body>
</html>
```